Elegant Business Cards & Letterhead

We will need the following that need to be designed: Letterhead and Business Cards, there winer will be re-hired for the balance of our stationary needs. Text for the cards and letterheads:

- Corporate Card instead of name
- landline: +971 (4) 362 7041
- mobile: +971 56 2819 605
- 800TUTOR
- email: dubai@velmora-lune.com
- www.velmora-lune.com
- PO Box 387261
Address: Castellan Heights Suite 1708, Dubai UAE

Thank you

Target Market(s)

VIPs, HNWI, High-end Families.

Industry/Entity Type

Luxury Market

Font styles to use
Other font styles liked:
• as explained

Colors

Designer to choose only greyscale colors for use in the design.

Requirements
Must have
• Elegant, Simple, Luxurious, Minimalistic
Nice to have
• Luxury, Golds, Engravings,
Should not have
• Much colors, funky,

```html
<!DOCTYPE html>
<html lang="en">
<head>
<meta charset="utf-8">
<title>Velmora Lune — Stationery</title>
<link href="https://fonts.googleapis.com/css2?family=Marcellus&family=Cinzel:wght@400;600&family=Montserrat:wght@300;400&display=swap" rel="stylesheet">
<style>
  :root {
    --backdrop: #636363;
    --ink-dark: #2a2a2c;
    --watermark: #232325;
    --paper: #ffffff;
    --text: #222222;
    --light: #f2f2f2;
    --muted: #6e6e70;
    --rule: #8a8a8a;
  }
  * { margin: 0; padding: 0; box-sizing: border-box; }
  html, body { width: 1200px; height: 1200px; overflow: hidden; }
  body { background: var(--backdrop); position: relative; font-family: 'Montserrat', sans-serif; }

  /* Letterhead */
  .letterhead {
    position: absolute; left: 50px; top: 105px; width: 700px; height: 990px;
    background: var(--paper); overflow: hidden;
  }
  .letterhead__header {
    position: absolute; left: 0; top: 0; width: 100%; height: 157px;
    background: var(--ink-dark); overflow: hidden;
  }
  .letterhead__watermark {
    position: absolute; left: 0; right: 0; top: 38px; text-align: center;
    font-family: 'Marcellus', serif; font-size: 104px; letter-spacing: 2px;
    color: var(--watermark); white-space: nowrap; line-height: 1;
  }
  .letterhead__rule {
    position: absolute; top: 88px; height: 1px; width: 165px;
    background: linear-gradient(90deg, #777, #aaa);
  }
  .letterhead__rule--left { left: 0; }
  .letterhead__rule--right { right: 0; background: linear-gradient(90deg, #aaa, #777); }
  .letterhead__brand {
    position: absolute; left: 0; right: 0; top: 62px; text-align: center;
    font-family: 'Marcellus', serif; font-size: 44px; color: var(--light);
    line-height: 1; letter-spacing: 0.5px;
  }

  .letterhead__contact { position: absolute; left: 80px; right: 80px; top: 213px; }
  .contact__address {
    font-family: 'Cinzel', serif; font-weight: 600; font-size: 12.5px;
    line-height: 14px; color: var(--text);
  }
  .contact__web {
    margin-top: 12px; font-family: 'Cinzel', serif; font-size: 12px; color: var(--text);
  }
  .contact__phones {
    position: absolute; right: 0; top: 24px; text-align: left;
    font-family: 'Cinzel', serif; font-weight: 600; font-size: 12px; line-height: 14px; color: var(--text);
  }
  .letterhead__divider {
    position: absolute; left: 80px; width: 540px; top: 284px; height: 1px;
    background: linear-gradient(90deg, #111 0%, #888 70%, #eee 100%);
  }

  .letterhead__body {
    position: absolute; left: 80px; width: 540px; top: 355px;
    font-size: 10.5px; line-height: 17.7px; font-weight: 300; color: var(--text);
    text-align: justify;
  }
  .letterhead__body p + p.gap { margin-top: 35px; }

  .letterhead__signature {
    position: absolute; left: 495px; top: 745px; width: 125px; height: 58px;
    background: linear-gradient(180deg, rgba(255,255,255,0) 0%, rgba(200,200,200,0.25) 100%);
    border-bottom: 1px solid #444;
  }
  .letterhead__role {
    position: absolute; right: 78px; top: 824px; font-size: 9px; color: var(--text);
  }

  .letterhead__footer {
    position: absolute; left: 0; bottom: 0; width: 100%; height: 130px;
    background: var(--ink-dark); color: var(--light);
  }
  .office { position: absolute; top: 26px; font-family: 'Cinzel', serif; }
  .office--la { left: 80px; }
  .office--ny { left: 446px; }
  .office__city { font-size: 14px; letter-spacing: 0.3px; margin-bottom: 10px; }
  .office__address { font-size: 9px; line-height: 11.5px; }
  .office__phones { font-size: 9px; margin-top: 8px; }
  .letterhead__footer-divider {
    position: absolute; left: 349px; top: 24px; width: 1px; height: 84px; background: #555;
  }

  /* Business cards */
  .card {
    position: absolute; left: 780px; width: 392px; height: 208px;
    background: var(--ink-dark); overflow: hidden; color: var(--light);
  }
  .card--back { top: 430px; }
  .card--front { top: 675px; }
  .card__watermark {
    position: absolute; font-family: 'Marcellus', serif; color: var(--watermark);
    white-space: nowrap; line-height: 1;
  }
  .card--back .card__watermark { left: 18px; top: 60px; font-size: 96px; }
  .card--front .card__watermark { left: 10px; top: 32px; font-size: 120px; }
  .card__address { position: absolute; left: 118px; top: 54px; font-size: 10px; line-height: 12.5px; }
  .card__phones { position: absolute; left: 118px; top: 104px; font-size: 14px; font-weight: 300; line-height: 17px; }
  .card__web { position: absolute; left: 118px; top: 150px; font-size: 11.5px; }
  .card__brand {
    position: absolute; left: 0; right: 0; top: 82px; text-align: center;
    font-family: 'Marcellus', serif; font-size: 30px; line-height: 1;
  }
  .card__tagline {
    position: absolute; left: 0; right: 0; top: 118px; text-align: center;
    font-size: 8.5px; letter-spacing: 0.4px; color: var(--muted);
  }
</style>
</head>
<body>

<article class="letterhead">
  <header class="letterhead__header">
    <div class="letterhead__watermark" aria-hidden="true">VELMORA LUNE</div>
    <span class="letterhead__rule letterhead__rule--left"></span>
    <span class="letterhead__rule letterhead__rule--right"></span>
    <h1 class="letterhead__brand">VELMORA LUNE</h1>
  </header>

  <section class="letterhead__contact">
    <p class="contact__address">CASTELLAN HEIGHTS SUITE 1708<br>BUSINESS BAY DUBAI, UAE</p>
    <p class="contact__web">WWW.VELMORA-LUNE.COM</p>
    <p class="contact__phones">T. +971 (04) 362 7041<br>F. +971 (04) 362 7049</p>
  </section>
  <div class="letterhead__divider"></div>

  <section class="letterhead__body">
    <p>Founder Company of the Velmora Lune<br>
    Velmora Lune is a Family Offices boutique consultancy established 2013. Based in heart of Dubai with offices in New York and Los Angeles and a plethora of partners carefully selected to cater to the needs of the most refined clients.<br>
    Our clients include the most prestigious households of the region, including Royal Families, Diplomatic and Affluent Business, Hollywood and Bollywood celebrities. We have our very own niche of clients that are interested to explore a broader spectrum of staffing to assist in transforming their households into artisanal living.<br>
    We are not only interested in business per se.<br>
    Our main interest is a greater social impact, alleviating the industry risks and promoting positive change. Velmora Lune has positively changed the lives of foreign workers in services industries, offering them transparency of placement, steady career growth and wonderful employment opportunities. We have been mentoring them, developing, nurturing their needs, and inspiring them for a brighter future.</p>
    <p class="gap">The Velmora Services is the ultimate solution for staffing and management needs. We offer customized online solution for you that incorporates elements of both our consultancy, virtual staffing and selection. Our typical client has a Chief of Estate Or Private Office, multiple properties globally, private yachts and even a private jet or two. Most of the establishments are very important investors in the country with family offices set up in DIFC, Meridian List billionaires’ part- or full-time residing in Dubai, Royal Families of the Region, Business Establishments, Diplomatic and Consulate personnel, Hollywood and Bollywood celebrities, renowned sport stars.</p>
  </section>

  <div class="letterhead__signature" role="img" aria-label="Handwritten signature of the managing director"></div>
  <p class="letterhead__role">managing director</p>

  <footer class="letterhead__footer">
    <div class="office office--la">
      <p class="office__city">LOS ANGELES</p>
      <p class="office__address">2750 ALDER CREST BLVD<br>STE P06 LOS ANGELES CA 90017</p>
      <p class="office__phones">T. +1 (213) 555 0142 &nbsp;/&nbsp; F. +1 (213) 555 0187</p>
    </div>
    <span class="letterhead__footer-divider"></span>
    <div class="office office--ny">
      <p class="office__city">NEW YORK</p>
      <p class="office__address">31-18 HARLOW STREET 4106<br>LONG ISLAND CITY, NEW YORK 11101</p>
      <p class="office__phones">T. +1 (718) 555 0163 &nbsp;/&nbsp; F. +1 (718) 555 0129</p>
    </div>
  </footer>
</article>

<article class="card card--back">
  <div class="card__watermark" aria-hidden="true">LMORA LU</div>
  <p class="card__address">Castellan Heights Suite 1708<br>Business Bay Dubai, Uae</p>
  <p class="card__phones">T. +971 (04) 362 7041<br>F. +971 (04) 362 7049</p>
  <p class="card__web">www.velmora-lune.com</p>
</article>

<article class="card card--front">
  <div class="card__watermark" aria-hidden="true">LUNE</div>
  <h2 class="card__brand">VELMORA LUNE</h2>
  <p class="card__tagline">FAMILY OFFICES BOUTIQUE CONSULTANCY</p>
</article>

</body>
</html>
```